Cosmetics Brand Logo and Bottle Label Design

We are creating a new cosmetics brand called "Nolan Whitby" and would like you to create an amazing logo and bottle label for this brand's new 100% pure argan oil product.
For the logo, we really like the logo's of Marin Calloway and Vessa. The text should be Sans Serif (without feet).
For the actual bottle label, please find attached labels of one of our competitors design which really like. We really like the simplicity and elegance of the design. The only difference is that our product will be using light turqoise as the brand color. Please feel free to add your own creativity into it as well.
Industry/Entity Type
Cosmetics
Logo Text
Nolan Whitby
Font styles to use

```html
<!DOCTYPE html>
<html lang="en">
<head>
<meta charset="utf-8">
<title>Nolan Whitby – Argan Oil Packaging</title>
<link href="https://fonts.googleapis.com/css2?family=Abel&family=Open+Sans:wght@400;700&display=swap" rel="stylesheet">
<style>
  :root {
    --teal: #2fb2a2;
    --teal-soft: #7cc7bd;
    --amber: #c2551c;
    --box: #e7e8ea;
    --label: #e3e4e6;
    --bg: #d9dadc;
  }
  html, body {
    margin: 0;
    width: 1200px;
    height: 1200px;
    overflow: hidden;
  }
  body {
    background: var(--bg);
    position: relative;
    font-family: "Abel", sans-serif;
    color: var(--teal);
  }
  .panel { position: absolute; background: var(--box); }
  .box-front { left: 200px; top: 110px; width: 352px; height: 978px; }
  .bottle-label { left: 720px; top: 360px; width: 300px; height: 650px; background: var(--label); border-radius: 26px 26px 4px 4px; }

  .abs { position: absolute; }
  .center-x { left: 0; right: 0; text-align: center; }

  .badge-shape {
    border-radius: 50%;
    box-sizing: border-box;
  }
  .badge-box { border: 3px solid var(--teal); }
  .badge-label { border: 4px solid var(--amber); background: var(--label); }

  .ornament { background: linear-gradient(to right, transparent, var(--teal-soft) 20%, var(--teal-soft) 80%, transparent); opacity: .35; border-radius: 30px; }

  .brand { font-family: "Abel", sans-serif; letter-spacing: 1px; white-space: nowrap; }
  .tagline { font-family: "Abel", sans-serif; letter-spacing: 1px; }

  .kicker, .headline, .subhead, .body-copy { font-family: "Open Sans", sans-serif; margin: 0; }
  .kicker { font-weight: 700; }
  .headline { font-weight: 700; white-space: nowrap; }
  .subhead { font-weight: 400; }
  .body-copy { font-weight: 400; }

  .icon-ring {
    border: 2px solid var(--teal);
    border-radius: 50%;
    box-sizing: border-box;
    display: flex; align-items: center; justify-content: center;
  }
  .icon-fill { border-radius: 50%; background: var(--teal); opacity: .85; }
</style>
</head>
<body>

<section class="panel box-front">
  <div class="abs badge-shape badge-box" role="img" aria-label="Natural product badge" style="left:98px; top:132px; width:156px; height:156px;"></div>

  <div class="abs ornament" role="img" aria-label="Decorative flourish" style="left:58px; top:418px; width:242px; height:52px;"></div>

  <div class="abs center-x brand" style="top:482px; font-size:45px;">Nolan Whitby</div>
  <div class="abs center-x tagline" style="top:536px; font-size:21px;">made from nature</div>

  <div class="abs ornament" role="img" aria-label="Decorative flourish" style="left:58px; top:566px; width:242px; height:56px;"></div>

  <div class="abs" style="left:39px; top:670px; width:240px;">
    <p class="kicker" style="font-size:12px;">LOREM IPSUM</p>
    <p class="headline" style="font-size:27px; line-height:30px;">DOLOR SIT AMET</p>
    <p class="subhead" style="font-size:17px; line-height:17px;">SAMPLE TEXT</p>
    <p class="body-copy" style="font-size:9.6px; line-height:11.2px;">Lorem ipsum dolor sit amet, consectetuer adipiscing elit, sed diam nonummy nibh euismod tincidunt ut laoreet dolore magna aliquam erat volutpat. Lorem ipsum dolor sit amet, consectetuer adipiscing elit, sed diam nonummy nibh euismod tincidunt ut laoreet dolore magna aliquam erat volutpat.</p>
  </div>

  <div class="abs icon-ring" style="left:42px; top:814px; width:80px; height:80px;">
    <div class="icon-fill" role="img" aria-label="Skin care profile icon" style="width:62px; height:62px;"></div>
  </div>
  <div class="abs icon-ring" style="left:138px; top:814px; width:80px; height:80px;">
    <svg width="34" height="46" viewBox="0 0 34 46" aria-label="Oil drop icon" role="img">
      <path d="M17 2 C 12 14, 3 22, 3 30 A 14 14 0 0 0 31 30 C 31 22, 22 14, 17 2 Z" fill="var(--teal)"/>
    </svg>
  </div>
  <div class="abs icon-ring" style="left:234px; top:814px; width:80px; height:80px;">
    <div class="icon-fill" role="img" aria-label="Plant leaf icon" style="width:62px; height:62px;"></div>
  </div>
</section>

<section class="panel bottle-label">
  <div class="abs badge-shape badge-label" role="img" aria-label="Natural product badge" style="left:62px; top:-98px; width:176px; height:176px;"></div>
  <svg class="abs" style="left:132px; top:114px;" width="36" height="50" viewBox="0 0 36 50" role="img" aria-label="Drop outline">
    <path d="M18 3 C 13 16, 4 24, 4 33 A 14 14 0 0 0 32 33 C 32 24, 23 16, 18 3 Z" fill="none" stroke="var(--amber)" stroke-width="4"/>
  </svg>

  <div class="abs ornament" role="img" aria-label="Decorative flourish" style="left:44px; top:212px; width:215px; height:44px;"></div>

  <div class="abs center-x brand" style="top:264px; font-size:40px;">Nolan Whitby</div>
  <div class="abs center-x tagline" style="top:314px; font-size:20px;">made from nature</div>

  <div class="abs ornament" role="img" aria-label="Decorative flourish" style="left:44px; top:350px; width:215px; height:44px;"></div>

  <div class="abs" style="left:26px; top:428px; width:200px;">
    <p class="kicker" style="font-size:11px;">LOREM IPSUM</p>
    <p class="headline" style="font-size:23px; line-height:25px;">DOLOR SIT AMET</p>
    <p class="subhead" style="font-size:14px; line-height:15px;">SAMPLE TEXT</p>
    <p class="body-copy" style="font-size:8px; line-height:9.6px;">Lorem ipsum dolor sit amet, consectetuer adipiscing elit, sed diam nonummy nibh euismod tincidunt ut laoreet dolore magna aliquam erat volutpat. Lorem ipsum dolor sit amet, consectetuer adipiscing elit, sed diam nonummy nibh euismod tincidunt ut laoreet.</p>
  </div>

  <div class="abs icon-ring" style="left:27px; top:567px; width:72px; height:72px;">
    <div class="icon-fill" role="img" aria-label="Skin care profile icon" style="width:56px; height:56px;"></div>
  </div>
  <div class="abs icon-ring" style="left:114px; top:567px; width:72px; height:72px;">
    <svg width="30" height="42" viewBox="0 0 34 46" aria-label="Oil drop icon" role="img">
      <path d="M17 2 C 12 14, 3 22, 3 30 A 14 14 0 0 0 31 30 C 31 22, 22 14, 17 2 Z" fill="var(--teal)"/>
    </svg>
  </div>
  <div class="abs icon-ring" style="left:202px; top:567px; width:72px; height:72px;">
    <div class="icon-fill" role="img" aria-label="Plant leaf icon" style="width:56px; height:56px;"></div>
  </div>
</section>

</body>
</html>
```